design a construction company business card

Design business card around our logo. Card must have all the typical info: name, title, address, phone, email, business name, etc. Somewhere on the card I would like to see our motto "Built with care... Driven by dedication." Consider adding a splash of bright orange to the card to complement the blues and silvers/grays in the logo. We are open to metallic inks, textures, etc. We would like to see options on both light and dark backgrounds. The font in the logo is Euro Technic Extended Regular.

```html
<!DOCTYPE html>
<html lang="en">
<head>
<meta charset="utf-8">
<title>Halden Builders – Business Card</title>
<link rel="stylesheet" href="https://fonts.googleapis.com/css2?family=Michroma&family=Open+Sans:wght@400;600&family=Roboto+Condensed:wght@400;500&display=swap">
<style>
  :root {
    --backdrop: #7b4b27;
    --kraft-light: #dbb98f;
    --kraft-mid: #c9a273;
    --kraft-dark: #b48c5d;
    --ink: #141008;
    --rule: #5c4630;
  }
  * { margin: 0; padding: 0; box-sizing: border-box; }
  html, body {
    width: 1200px;
    height: 900px;
    overflow: hidden;
  }
  body {
    position: relative;
    background: var(--backdrop);
    color: var(--ink);
    font-family: "Open Sans", sans-serif;
  }
  .card {
    position: absolute;
    left: 330px;
    width: 556px;
    height: 343px;
    background: radial-gradient(ellipse at 40% 20%, var(--kraft-light) 0%, var(--kraft-mid) 55%, var(--kraft-dark) 100%);
    text-align: center;
  }
  .card--back { top: 90px; }
  .card--front { top: 470px; }

  .contact-name {
    position: absolute;
    top: 62px;
    left: 0; right: 0;
    font-family: "Michroma", sans-serif;
    font-weight: 400;
    font-size: 19px;
    letter-spacing: 1px;
    line-height: 26px;
  }
  .contact-title {
    position: absolute;
    top: 86px;
    left: 0; right: 0;
    font-size: 15.5px;
    line-height: 20px;
  }
  .divider {
    position: absolute;
    left: 181px;
    width: 195px;
    height: 1px;
    background: var(--rule);
  }
  .divider--upper { top: 117px; }
  .divider--lower { top: 222px; }
  .contact-lines {
    position: absolute;
    top: 129px;
    left: 0; right: 0;
    list-style: none;
    font-size: 15.5px;
    line-height: 20px;
  }
  .contact-lines b { font-weight: 600; }
  .address {
    position: absolute;
    top: 239px;
    left: 0; right: 0;
    font-size: 15.5px;
    line-height: 20px;
    font-style: normal;
  }

  .company-name {
    position: absolute;
    top: 130px;
    left: 0; right: 0;
    font-family: "Roboto Condensed", sans-serif;
    font-weight: 500;
    font-size: 46px;
    line-height: 54px;
    letter-spacing: 1px;
    text-transform: uppercase;
  }
  .motto {
    position: absolute;
    top: 268px;
    left: 0; right: 0;
    font-family: "Roboto Condensed", sans-serif;
    font-weight: 400;
    font-size: 15px;
    line-height: 20px;
    text-transform: uppercase;
  }
</style>
</head>
<body>
  <section class="card card--back" aria-label="Contact side">
    <h1 class="contact-name">DANIEL HART</h1>
    <p class="contact-title">Managing Director</p>
    <div class="divider divider--upper"></div>
    <ul class="contact-lines">
      <li><b>P:</b> 044-123 456 789</li>
      <li><b>M:</b> 044-123 456 789</li>
      <li><b>E:</b> info@webname.com</li>
      <li><b>W:</b> www.websitename.com</li>
    </ul>
    <div class="divider divider--lower"></div>
    <address class="address">12345, Address Goes Here<br>Country Name, 123456.</address>
  </section>

  <section class="card card--front" aria-label="Company side">
    <h2 class="company-name">Halden Builders, Inc.</h2>
    <p class="motto">Built with care... Driven by dedication</p>
  </section>
</body>
</html>
```